Cozy Sprouts Business Cards

I need a business card for my new Company called Cozy Sprouts. We create handmade baby moccasins, headbands, t-shirts and more. I want some that will appeal to parents, and to go with the colors of my logo that I have attached. feel free to be creative. I would like my logo placed somewhere on the card.

Industry/Entity Type

Retail

Contact Information for Business Card

Cozy Sprouts
24816 Maplecrest D #5172
Irvine Ca 92738
Rosalind Vantrey Ceo
Info@Cozy-Sprouts.com
www.Cozy-Sprouts.com
Phone 9495817320

Requirements
Nice to have
• Logo included

```html
<!DOCTYPE html>
<html lang="en">
<head>
<meta charset="utf-8">
<title>Cozy Sprouts Business Card</title>
<link rel="stylesheet" href="https://fonts.googleapis.com/css2?family=Varela+Round&family=Open+Sans:wght@400;600;700&display=swap">
<style>
  :root {
    --page-bg: #ecebe8;
    --card-bg: #ffffff;
    --ink-dark: #1f1f1f;
    --ink-grey: #6b6b6b;
    --accent: #e8895a;
    --accent-light: #efa783;
    --accent-dark: #c9683a;
    --divider: #555555;
  }
  * { margin: 0; padding: 0; box-sizing: border-box; }
  html, body {
    width: 1200px; height: 1022px; overflow: hidden;
    background: var(--page-bg);
  }
  .business-card {
    position: absolute; left: 75px; top: 211px;
    width: 1050px; height: 600px;
    background: linear-gradient(160deg, #ffffff 0%, #f4f4f4 100%);
    border-radius: 14px;
    overflow: hidden;
    box-shadow: 0 10px 30px rgba(0,0,0,0.18);
    font-family: "Open Sans", sans-serif;
  }
  .company-name {
    position: absolute; left: 330px; top: 120px;
    font-family: "Varela Round", sans-serif;
    font-size: 84px; line-height: 1;
    color: var(--ink-dark);
    letter-spacing: 1px;
  }
  .logo-mark {
    position: absolute; left: 110px; top: 265px;
    width: 150px; height: 150px;
    background: var(--accent);
    border-radius: 14px;
  }
  .divider {
    position: absolute; left: 575px; top: 265px;
    height: 190px; border-left: 2px dashed var(--divider);
  }
  .contact-list {
    position: absolute; right: 490px; top: 290px;
    list-style: none; text-align: right;
  }
  .contact-list li {
    display: flex; justify-content: flex-end; align-items: center;
    gap: 16px; height: 42px;
    font-size: 22px; color: var(--accent-light);
  }
  .contact-list svg { width: 20px; height: 20px; flex: none; }
  .person {
    position: absolute; left: 605px; top: 262px;
  }
  .person-name {
    font-size: 38px; font-weight: 700; color: var(--accent);
    line-height: 1.2;
  }
  .person-role {
    font-size: 20px; color: var(--ink-grey); margin-top: 6px;
  }
  .address {
    margin-top: 14px; font-size: 23px; line-height: 1.35;
    color: var(--accent-light);
  }
  .accent-band {
    position: absolute; left: 0; bottom: 0;
    width: 100%; height: 86px;
    background: linear-gradient(180deg, var(--accent-light) 0%, var(--accent) 60%, var(--accent-dark) 100%);
  }
</style>
</head>
<body>
  <article class="business-card">
    <div class="logo-mark" aria-hidden="true"></div>
    <h1 class="company-name">Cozy Sprouts</h1>

    <ul class="contact-list">
      <li><span>9495817320</span>
        <svg viewBox="0 0 20 20" aria-hidden="true"><path d="M5 2 L8 2 L9 6 L7 8 Q9 12 12 13 L14 11 L18 12 L18 15 Q18 18 15 18 Q3 16 2 5 Q2 2 5 2 Z" fill="none" stroke="#444" stroke-width="1.6"/></svg></li>
      <li><span>www.Cozy-Sprouts.com</span>
        <svg viewBox="0 0 20 20" aria-hidden="true"><g fill="none" stroke="#444" stroke-width="1.5"><circle cx="10" cy="10" r="8"/><ellipse cx="10" cy="10" rx="3.5" ry="8"/><line x1="2" y1="10" x2="18" y2="10"/></g></svg></li>
      <li><span>Info@Cozy-Sprouts.com</span>
        <svg viewBox="0 0 20 20" aria-hidden="true"><g fill="none" stroke="#444" stroke-width="1.5"><rect x="2" y="4" width="16" height="12"/><polyline points="2,4 10,11 18,4"/></g></svg></li>
    </ul>

    <div class="divider" aria-hidden="true"></div>

    <section class="person">
      <p class="person-name">Rosalind Vantrey</p>
      <p class="person-role">Ceo</p>
      <p class="address">Cozy Sprouts 24816 Maplecrest D<br>#5172 Irvine Ca 92738</p>
    </section>

    <div class="accent-band" aria-hidden="true"></div>
  </article>
</body>
</html>
```